Investment Real Estate Firm Needs Template to Showcase properties

We're a firm that sells $1M-$20M Dollar properties. We need a very professional template to be able to insert our information, pictures, and data into it. The data is mostly send via email in PDF and/or printed out. Here's the templates we need using OUR Logo and colors. Name of Company: Harlow Capital Partners

1.)Cover Page Template: I've attached a example but we would like our own original cover page that looks cool and has spot for property photo
2.)Table of Contents Template: I've attached some cool original ideas that we like. Obviously would love our own
3.)Beginning of Section Template: Basically a page letting you know what section you're about ready to start.
4.) Content/Data Template: This is the template where all data will be inserted. So basically just bordering and very minimal space taken up to allow for content to be added
5.) Back Page/Last Page Template: This will be the last page of the presentation or showcase. I can also use this page to insert disclaimers and confidentiality language.

Target Market(s)

This only goes to a targeted personal client base

Industry/Entity Type

Real Estate

Font styles to use
Serif

Requirements
Must have
• - Cover Page, Contents Page, Section Page, Content Page, Back Page
• - Use our Logo. Attached
• - Use Our color scheme
• - Professional Look but some original ideas ;)
• - Abbility for me to edit and Drop in content
Nice to have
• Some Creativity in bordering and maybe carry over the section identity somehow within the border.
• A Extremely light but noticeable transparent "HCP" Logo Only on content pages in background centered " See attached

```html
<!DOCTYPE html>
<html lang="en">
<head>
<meta charset="utf-8">
<title>Harlow Capital Partners – Presentation Templates</title>
<link href="https://fonts.googleapis.com/css2?family=Crimson+Text:wght@400&family=Lato:wght@400;700&display=swap" rel="stylesheet">
<style>
:root{
  --gold:#cbbf96;
  --gold-line:#bfae7c;
  --ink:#1c1c1c;
  --panel:rgba(58,58,58,.9);
  --panel-solid:#3b3b3b;
  --footer:#0b0b0b;
  --paper:#e6e6e6;
  --text-light:#e9e6dc;
  --gap:#d4d4d4;
}
*{margin:0;padding:0;box-sizing:border-box}
html,body{width:850px;height:1200px;overflow:hidden;background:var(--gap)}
.sheet{width:850px;height:1200px;display:grid;grid-template-columns:424px 424px;grid-template-rows:repeat(5,238.4px);gap:2px;background:var(--gap)}
.slide{position:relative;overflow:hidden;background:var(--ink);font-family:"Lato",sans-serif;color:var(--text-light)}
.photo{position:absolute}
.bg{inset:0 0 24px 0}
.bg-dark{background:linear-gradient(160deg,#5a5a5a 0%,#2e2e2e 45%,#1a1a1a 100%)}
.bg-city{background:linear-gradient(180deg,#9a9a9a 0%,#6f6f6f 45%,#3d3d3d 100%)}
.bg-sky{background:linear-gradient(180deg,#e4e4e4 0%,#cfcfcf 60%,#9c9c9c 100%)}
.panel{position:absolute;background:var(--panel)}
.rule{display:block;width:22px;height:2px;background:var(--gold);margin-bottom:8px}
.title{font-family:"Crimson Text",serif;font-weight:400;color:var(--gold);line-height:1.15}
.bullet{display:inline-block;width:9px;height:9px;background:var(--gold);flex:none}
.small{font-size:6px;line-height:1.45;color:var(--text-light)}
.footer{position:absolute;left:0;right:0;bottom:0;height:24px;background:var(--footer);display:flex;align-items:center;justify-content:space-between;padding:0 22px}
.footer .mark{font-family:"Crimson Text",serif;font-size:13px;color:#cfcfcf;letter-spacing:.5px}
.footer .url{font-size:4.5px;color:#bdbdbd;letter-spacing:.2px}
.footer .page{width:13px;height:13px;background:var(--gold);color:var(--ink);font-size:6px;display:flex;align-items:center;justify-content:center;margin-right:-8px}
.icon-box{position:absolute;width:46px;height:46px;background:var(--gold);display:flex;align-items:center;justify-content:center}
.icon-box svg{width:30px;height:30px}

/* cover */
.cover-name{position:absolute;left:0;right:0;top:78px;text-align:center;font-family:"Crimson Text",serif;font-size:22px;letter-spacing:1.5px;color:#e2e2e2}
.cover-rule{position:absolute;left:135px;right:135px;top:118px;height:1px;background:#bdbdbd}
.cover-intro{position:absolute;left:55px;top:163px;width:305px;display:flex;gap:12px}
/* toc */
.toc-list{list-style:none;margin-top:10px}
.toc-list li{display:flex;align-items:center;gap:17px;font-size:7.5px;color:var(--gold);height:23px}
/* icon columns */
.subject{position:absolute;width:70px;text-align:center}
.subject h3{font-family:"Crimson Text",serif;font-weight:400;font-size:10px;color:var(--gold);margin:7px 0 6px}
.subject p{font-size:4.8px;line-height:1.5;color:#cfcfcf}
.divider{position:absolute;width:1px;background:var(--gold-line)}
/* numbered */
.num{position:absolute;left:345px;width:78px}
.num b{display:block;font-family:"Crimson Text",serif;font-weight:400;font-size:12px;color:var(--gold);line-height:1}
.num span{display:block;font-size:4.6px;color:#cfcfcf;line-height:1.5;margin-top:2px}
/* contact */
.contact-row{display:flex;align-items:center;gap:10px;font-size:7px;color:#eee;height:29px}
.contact-row .ic{width:17px;height:17px;background:var(--gold);display:flex;align-items:center;justify-content:center;flex:none}
.contact-row svg{width:11px;height:11px}
/* legal */
.legal p{font-size:5.4px;line-height:1.5;color:#e4e4e4;margin-bottom:7px}
</style>
</head>
<body>
<main class="sheet">

  <!-- 1 Cover -->
  <section class="slide cover">
    <div class="photo bg bg-dark" style="inset:0" role="img" aria-label="Property photograph: looking up at dark glass skyscrapers"></div>
    <div class="cover-name">HARLOW CAPITAL PARTNERS</div>
    <div class="cover-rule"></div>
    <div class="cover-intro">
      <span class="bullet" style="width:11px;height:11px"></span>
      <p class="small" style="font-size:5.6px">Lorem ipsum dolor sit amet, consectetuer adipiscing elit. Maecenas porttitor congue massa. Fusce posuere, magna sed pulvinar ultricies, purus lectus malesuada libero, sit amet commodo magna eros quis urna. Nunc viverra imperdiet enim. Fusce est. Vivamus a tellus.</p>
    </div>
  </section>

  <!-- 2 Table of Contents -->
  <section class="slide toc">
    <div class="photo bg bg-city" role="img" aria-label="Background photograph of a city skyline"></div>
    <div class="panel" style="left:24px;top:0;width:232px;bottom:24px;padding:26px 0 0 12px">
      <span class="rule"></span>
      <h2 class="title" style="font-size:18px">Table Of Contents</h2>
      <ul class="toc-list">
        <li><span class="bullet"></span>Lorem ipsum dolor sit amet, consectetuer</li>
        <li><span class="bullet"></span>Fusce posuere, magna sed pulvinar ultricies</li>
        <li><span class="bullet"></span>Nunc viverra imperdiet enim</li>
        <li><span class="bullet"></span>Fusce est. Vivamus a tellus</li>
        <li><span class="bullet"></span>Pellentesque habitant morbi tristique senectus</li>
        <li><span class="bullet"></span>Mauris et orci.</li>
      </ul>
    </div>
    <div class="photo" style="left:256px;top:0;width:89px;bottom:24px;background:linear-gradient(160deg,#d8e3ec 0%,#8a97a3 45%,#7a4a36 100%)" role="img" aria-label="Photograph of a glass tower beside a brick building"></div>
    <div style="position:absolute;left:345px;top:0;width:46px;bottom:24px;background:var(--gold)"></div>
    <footer class="footer"><span class="mark">HCP</span><span class="url">www.HarlowCapitalPartners.com</span><span class="page">2</span></footer>
  </section>

  <!-- 3 Section Header -->
  <section class="slide section-header">
    <div class="photo bg bg-city" role="img" aria-label="Background photograph of a waterfront city"></div>
    <div class="panel" style="left:44px;top:0;width:186px;bottom:24px;padding:64px 0 0 12px">
      <span class="rule"></span>
      <h2 class="title" style="font-size:20px;line-height:1.25">Section<br>Header<br>Slide</h2>
      <div style="display:flex;gap:8px;margin-top:8px">
        <span class="bullet"></span>
        <p class="small" style="font-size:5.8px">Lorem ipsum dolor sit amet, consectetuer adipiscing elit. Maecenas porttitor congue</p>
      </div>
    </div>
    <div class="photo" style="left:230px;top:0;width:128px;bottom:24px;background:linear-gradient(180deg,#a9c6e0 0%,#e6e9ec 55%,#7d7f83 100%)" role="img" aria-label="Photograph of an engineer in a hard hat holding a tablet"></div>
    <div style="position:absolute;left:358px;top:0;width:1px;bottom:24px;background:var(--gold-line)"></div>
    <footer class="footer"><span class="mark">HCP</span><span class="url">www.HarlowCapitalPartners.com</span><span class="page">3</span></footer>
  </section>

  <!-- 4 Content -->
  <section class="slide content">
    <div class="photo bg bg-sky" role="img" aria-label="Faded background photograph of a skyline"></div>
    <div style="position:absolute;left:36px;top:20px">
      <span class="rule"></span>
      <h2 class="title" style="font-size:20px;color:#111">Content Slide</h2>
    </div>
    <div class="photo" style="left:36px;top:54px;width:364px;height:158px;background:linear-gradient(180deg,#5d5d5d 0%,#4a4a4a 60%,#333 100%)" role="img" aria-label="Content area showing a dark skyline photograph"></div>
    <footer class="footer"><span class="mark">HCP</span><span class="url">www.HarlowCapitalPartners.com</span><span class="page">4</span></footer>
  </section>

  <!-- 5 Features with photos -->
  <section class="slide features">
    <div class="photo bg bg-sky" role="img" aria-label="Faded background photograph of a harbour"></div>
    <div class="photo" style="left:36px;top:0;width:172px;height:78px;background:linear-gradient(135deg,#1f5f9a 0%,#67a9d6 50%,#1c3554 100%)" role="img" aria-label="Photograph of a glass facade with steel cross bracing"></div>
    <div class="photo" style="left:214px;top:0;width:172px;height:118px;background:linear-gradient(160deg,#6f8a4c 0%,#d9d5c6 55%,#b98a4a 100%)" role="img" aria-label="Photograph of an atrium with a tree and glass walls"></div>
    <div class="photo" style="left:214px;top:123px;width:210px;height:91px;background:linear-gradient(150deg,#2d5a66 0%,#8fb3bd 50%,#1e3a42 100%)" role="img" aria-label="Photograph of a glass curtain wall"></div>
    <div class="panel" style="left:36px;top:87px;width:172px;height:127px;padding:12px 0 0 10px">
      <span class="rule"></span>
      <h2 class="title" style="font-size:13.5px">Features With<br>Accompanying Photos</h2>
      <div style="display:flex;gap:10px;margin-top:8px;padding-right:10px">
        <span class="bullet"></span>
        <p class="small" style="font-size:5.6px">Lorem ipsum dolor sit amet, consectetuer adipiscing elit. Maecenas porttitor congue massa. Fusce posuere, magna sed pulvinar ultricies, purus lectus malesuada libero, sit amet</p>
      </div>
    </div>
    <footer class="footer"><span class="mark">HCP</span><span class="url">www.HarlowCapitalPartners.com</span><span class="page">5</span></footer>
  </section>

  <!-- 6 Explanation with iconography -->
  <section class="slide iconography">
    <div class="photo bg bg-city" role="img" aria-label="Background photograph of a tower above the city"></div>
    <div class="panel" style="left:0;right:0;top:42px;height:158px"></div>
    <div style="position:absolute;left:36px;top:66px">
      <span class="rule"></span>
      <h2 class="title" style="font-size:15px;line-height:1.3">Explanation<br>With<br>Iconography</h2>
    </div>
    <div class="icon-box" style="left:172px;top:63px"><svg viewBox="0 0 30 30"><circle cx="15" cy="15" r="12" fill="none" stroke="#111" stroke-width="2.2"/><polyline points="8,19 12,13 16,17 22,9" fill="none" stroke="#111" stroke-width="2.2"/></svg></div>
    <div class="icon-box" style="left:252px;top:63px"><svg viewBox="0 0 30 30"><path d="M15 3 A12 12 0 1 0 27 15 L15 15 Z" fill="#111"/><path d="M17 1 A12 12 0 0 1 29 13 L17 13 Z" fill="#111"/></svg></div>
    <div class="icon-box" style="left:332px;top:63px"><svg viewBox="0 0 30 30"><circle cx="12" cy="12" r="8" fill="none" stroke="#111" stroke-width="3"/><line x1="18" y1="18" x2="26" y2="26" stroke="#111" stroke-width="4"/></svg></div>
    <div class="divider" style="left:240px;top:82px;height:100px"></div>
    <div class="divider" style="left:320px;top:82px;height:100px"></div>
    <div class="subject" style="left:160px;top:108px"><h3>Subject</h3><p>Nunc viverra imperdiet enim. Fusce est. Vivamus a tellus. Lorem ipsum dolor sit amet, consectetuer adipiscing elit. Maecenas porttitor congue massa.</p></div>
    <div class="subject" style="left:240px;top:108px"><h3>Subject</h3><p>Nunc viverra imperdiet enim. Fusce est. Vivamus a tellus. Lorem ipsum dolor sit amet, consectetuer adipiscing elit. Maecenas porttitor congue massa.</p></div>
    <div class="subject" style="left:320px;top:108px"><h3>Subject</h3><p>Nunc viverra imperdiet enim. Fusce est. Vivamus a tellus. Lorem ipsum dolor sit amet, consectetuer adipiscing elit. Maecenas porttitor congue massa.</p></div>
    <footer class="footer"><span class="mark">HCP</span><span class="url">www.HarlowCapitalPartners.com</span><span class="page">6</span></footer>
  </section>

  <!-- 7 Explanation, iconography & photo -->
  <section class="slide icon-photo">
    <div class="photo bg" style="background:linear-gradient(180deg,#4a4a4a 0%,#3a3a3a 60%,#5c5c5c 100%)" role="img" aria-label="Background photograph of a city at dusk"></div>
    <div style="position:absolute;left:36px;top:52px">
      <span class="rule"></span>
      <h2 class="title" style="font-size:15px;line-height:1.3">Explanation,<br>Iconography<br>&amp; Photo</h2>
    </div>
    <div class="photo" style="left:142px;top:0;width:128px;bottom:24px;background:linear-gradient(160deg,#2a4f79 0%,#7eb0d6 45%,#e8e2b8 70%,#1a2535 100%)" role="img" aria-label="Photograph of two business people shaking hands by a window"></div>
    <div class="icon-box" style="left:296px;top:9px"><svg viewBox="0 0 30 30"><circle cx="15" cy="15" r="12" fill="none" stroke="#111" stroke-width="2.2"/><polyline points="8,19 12,13 16,17 22,9" fill="none" stroke="#111" stroke-width="2.2"/></svg></div>
    <div class="icon-box" style="left:296px;top:85px"><svg viewBox="0 0 30 30"><circle cx="12" cy="12" r="8" fill="none" stroke="#111" stroke-width="3"/><line x1="18" y1="18" x2="26" y2="26" stroke="#111" stroke-width="4"/></svg></div>
    <div class="icon-box" style="left:296px;top:160px"><svg viewBox="0 0 30 30"><path d="M15 3 A12 12 0 1 0 27 15 L15 15 Z" fill="#111"/><path d="M17 1 A12 12 0 0 1 29 13 L17 13 Z" fill="#111"/></svg></div>
    <div class="num" style="top:20px"><b>01</b><span>Nunc viverra imperdiet enim. Fusce est. Vivamus a tellus.</span></div>
    <div class="num" style="top:96px"><b>02</b><span>Nunc viverra imperdiet enim. Fusce est. Vivamus a tellus.</span></div>
    <div class="num" style="top:171px"><b>03</b><span>Nunc viverra imperdiet enim. Fusce est. Vivamus a tellus.</span></div>
    <footer class="footer"><span class="mark">HCP</span><span class="url">www.HarlowCapitalPartners.com</span><span class="page">7</span></footer>
  </section>

  <!-- 8 Mission Statement -->
  <section class="slide mission">
    <div class="photo bg bg-dark" role="img" aria-label="Background photograph of a skyline"></div>
    <div style="position:absolute;left:24px;top:18px">
      <span class="rule"></span>
      <h2 class="title" style="font-size:15px">Mission Statement</h2>
    </div>
    <div class="photo" style="left:24px;top:49px;width:387px;height:92px;background:linear-gradient(180deg,#a9b8d6 0%,#6d6aa0 45%,#c98a4a 75%,#2e2c3e 100%)" role="img" aria-label="Photograph of a city skyline lit at dusk"></div>
    <div style="position:absolute;left:24px;top:141px;width:387px;height:56px;background:var(--gold);padding:8px 16px">
      <p style="font-size:7.2px;line-height:1.5;color:#1a1a1a">Nunc viverra imperdiet enim. Fusce est. Vivamus a tellus. Lorem ipsum dolor sit amet, consectetuer adipiscing elit. Maecenas porttitor congue massa. Nunc viverra imperdiet enim. Fusce est. Vivamus a tellus. Lorem ipsum dolor sit amet, consectetuer adipiscing elit. Maecenas porttitor congue massa.</p>
    </div>
    <footer class="footer"><span class="mark">HCP</span><span class="url">www.HarlowCapitalPartners.com</span><span class="page">8</span></footer>
  </section>

  <!-- 9 Contact -->
  <section class="slide contact">
    <div class="photo bg bg-city" role="img" aria-label="Background aerial photograph of downtown towers"></div>
    <div class="panel" style="left:26px;top:0;width:172px;bottom:24px;padding:18px 0 0 10px">
      <span class="rule"></span>
      <h2 class="title" style="font-size:19px;margin-bottom:12px">Contact Us</h2>
      <div class="contact-row"><span class="ic"><svg viewBox="0 0 12 12"><path d="M2.5 1 L4.5 1 L5 3.5 L3.8 4.4 C4.4 6 5.8 7.4 7.6 8.2 L8.5 7 L11 7.5 L11 9.5 C11 10.3 10.3 11 9.5 11 C5 11 1 7 1 2.5 C1 1.7 1.7 1 2.5 1 Z" fill="#111"/></svg></span>555.014.2290</div>
      <div class="contact-row"><span class="ic"><svg viewBox="0 0 12 12"><rect x="1" y="2.5" width="10" height="7" fill="none" stroke="#111" stroke-width="1.2"/><polyline points="1,2.5 6,7 11,2.5" fill="none" stroke="#111" stroke-width="1.2"/></svg></span>info@HarlowCapitalPartners.com</div>
      <div class="contact-row"><span class="ic"><svg viewBox="0 0 12 12"><circle cx="6" cy="6" r="5" fill="none" stroke="#111" stroke-width="1.1"/><ellipse cx="6" cy="6" rx="2.2" ry="5" fill="none" stroke="#111" stroke-width="1"/><line x1="1" y1="6" x2="11" y2="6" stroke="#111" stroke-width="1"/></svg></span>www.HarlowCapitalPartners.com</div>
      <div class="contact-row" style="height:34px"><span class="ic"><svg viewBox="0 0 12 12"><path d="M6 11 C3.5 8 2.5 6.2 2.5 4.5 A3.5 3.5 0 0 1 9.5 4.5 C9.5 6.2 8.5 8 6 11 Z" fill="#111"/><circle cx="6" cy="4.5" r="1.3" fill="var(--gold)"/></svg></span><span>480 Harbor Row<br>Bayview, CA 90000</span></div>
    </div>
    <footer class="footer"><span class="mark">HCP</span><span class="url">www.HarlowCapitalPartners.com</span><span class="page">9</span></footer>
  </section>

  <!-- 10 Legal -->
  <section class="slide legal">
    <div class="photo bg bg-city" role="img" aria-label="Background photograph of a city skyline"></div>
    <div class="panel" style="left:24px;top:0;width:376px;bottom:24px;padding:18px 14px 0 14px">
      <span class="rule"></span>
      <h2 class="title" style="font-size:19px;margin-bottom:6px;color:#f0ede4">Legal Disclaimer</h2>
      <p>Lorem ipsum dolor sit amet, consectetuer adipiscing elit. Maecenas porttitor congue massa. Fusce posuere, magna sed pulvinar ultricies, purus lectus malesuada libero, sit amet commodo magna eros quis urna.</p>
      <p>Nunc viverra imperdiet enim. Fusce est. Vivamus a tellus. Lorem ipsum dolor sit amet, consectetuer adipiscing elit. Maecenas porttitor congue massa. Fusce posuere, magna sed pulvinar ultricies, purus lectus malesuada libero, sit amet commodo magna eros quis urna.</p>
      <p>Nunc viverra imperdiet enim. Fusce est. Vivamus a tellus.</p>
      <p>Pellentesque habitant morbi tristique senectus et netus et malesuada fames ac turpis egestas. Proin pharetra nonummy pede. Mauris et orci.</p>
      <p>Pellentesque habitant morbi tristique senectus et netus et malesuada fames ac turpis egestas. Proin pharetra nonummy pede. Mauris et orci. Lorem ipsum dolor sit amet, consectetuer adipiscing elit. Maecenas porttitor congue massa. Fusce posuere, magna sed pulvinar ultricies, purus lectus malesuada libero, sit amet commodo magna eros quis urna.</p>
      <p>Pellentesque habitant morbi tristique senectus et netus et malesuada fames ac turpis egestas. Proin pharetra nonummy pede. Mauris et orci.</p>
    </div>
    <footer class="footer"><span class="mark">HCP</span><span class="url">www.HarlowCapitalPartners.com</span><span class="page">10</span></footer>
  </section>

</main>
</body>
</html>
```